VOREN Medical Industry and Symposium Banner

We need to design a banner for our organization that we can use at events and symposiums to advertise our company. We need to make a standing banner like this: https://www.printlodexa.com/products/signs-banners/banners/full-color-305-x-74-stand-up-banner/405500 and a hanging banner like this: https://www.printlodexa.com/products/signs-banners/banners/full-color-6-x-2-vinyl-banner/383000?quote_bc=2. Our goal is to summarize our organization with 3 to 5 bullet points of what we do and why customers may want to use us, our logo, and a slogan. We want the aesthetic to be clean, medical, modern, safe, and fun. Here's our website for reference material. https://www.vorenmedics.com/

Industry/Entity Type

Medical, EMS, Rescue, Occupational Safety

Requirements
Must have
• Logo, Slogan, List of at least 5 company highlights, modern and clean aesthetic.

```html
<!DOCTYPE html>
<html lang="en">
<head>
<meta charset="utf-8">
<title>VOREN Stand-up Banner</title>
<link href="https://fonts.googleapis.com/css2?family=Didact+Gothic&family=Montserrat:wght@800&display=swap" rel="stylesheet">
<style>
  :root {
    --brand-blue: #1e44a0;
    --white: #ffffff;
    --alert-red: #ec1c24;
    --sky-top: #d6d9df;
    --sky-bottom: #b9bdc4;
    --tarmac: #8a8d90;
  }
  html, body {
    margin: 0;
    padding: 0;
    overflow: hidden;
  }
  .banner {
    position: relative;
    width: 1200px;
    height: 2912px;
    background: var(--brand-blue);
    color: var(--white);
    font-family: "Didact Gothic", "Century Gothic", sans-serif;
    overflow: hidden;
  }
  .tagline {
    position: absolute;
    left: 158px;
    top: 100px;
    margin: 0;
    font-weight: 400;
    font-size: 62px;
    line-height: 80px;
    letter-spacing: -1px;
    text-transform: uppercase;
    transform: scaleX(0.88);
    transform-origin: left top;
    white-space: nowrap;
  }
  .service {
    position: absolute;
    left: 0;
    width: 1200px;
  }
  .service-icon {
    position: absolute;
    left: 77px;
    width: 131px;
    height: 131px;
  }
  .service-name {
    position: absolute;
    left: 271px;
    margin: 0;
    font-size: 79px;
    line-height: 90px;
    letter-spacing: 3px;
    font-weight: 400;
    -webkit-text-stroke: 1.2px var(--white);
  }
  .photo {
    position: absolute;
    left: 0;
    top: 1785px;
    width: 1200px;
    height: 582px;
    background: linear-gradient(to bottom, var(--sky-top) 0%, var(--sky-bottom) 60%, #7d8186 62%, var(--tarmac) 100%);
  }
  .slogan-band {
    position: absolute;
    left: 0;
    top: 2367px;
    width: 1200px;
    height: 150px;
    background: var(--alert-red);
    display: flex;
    align-items: center;
    justify-content: center;
  }
  .slogan {
    margin: 0;
    font-size: 70px;
    letter-spacing: 3px;
    font-weight: 400;
    -webkit-text-stroke: 1.2px var(--white);
  }
  .brand {
    position: absolute;
    left: 213px;
    top: 2536px;
    display: flex;
    align-items: center;
    gap: 50px;
  }
  .brand-dot {
    width: 290px;
    height: 290px;
    border-radius: 50%;
    background: var(--alert-red);
  }
  .brand-name {
    margin: 0;
    font-family: "Montserrat", "Didact Gothic", sans-serif;
    font-weight: 800;
    font-size: 150px;
    letter-spacing: 2px;
    color: var(--white);
  }
</style>
</head>
<body>
<main class="banner">
  <h2 class="tagline">Extensive services for all your<br>remote medial needs</h2>

  <section class="service" style="top:0">
    <svg class="service-icon" style="top:390px" viewBox="0 0 100 100" aria-hidden="true">
      <circle cx="50" cy="50" r="50" fill="#fff"/>
      <g stroke="#1e44a0" stroke-width="6" fill="none" stroke-linecap="round">
        <path d="M16 30 L28 24 L40 40 L84 40"/>
        <path d="M38 44 L66 74 M66 44 L38 74"/>
      </g>
      <circle cx="36" cy="77" r="5" fill="#1e44a0"/>
      <circle cx="68" cy="77" r="5" fill="#1e44a0"/>
    </svg>
    <h3 class="service-name" style="top:384px">Nationally Registered<br>Paramedics</h3>
  </section>

  <section class="service" style="top:0">
    <svg class="service-icon" style="top:639px" viewBox="0 0 100 100" aria-hidden="true">
      <circle cx="50" cy="50" r="50" fill="#fff"/>
      <g stroke="#1e44a0" stroke-width="5" fill="none" stroke-linecap="round">
        <circle cx="50" cy="30" r="12"/>
        <path d="M24 80 V66 Q24 50 50 50 Q76 50 76 66 V80"/>
        <path d="M38 52 V66 M38 66 a5 5 0 1 0 0.1 0 M62 52 V62 Q62 70 56 70 M62 62 Q62 70 68 70"/>
      </g>
    </svg>
    <h3 class="service-name" style="top:659px">Licensed Physicians</h3>
  </section>

  <section class="service" style="top:0">
    <svg class="service-icon" style="top:828px" viewBox="0 0 100 100" aria-hidden="true">
      <circle cx="50" cy="50" r="50" fill="#fff"/>
      <g stroke="#1e44a0" stroke-width="5" fill="none" stroke-linejoin="round">
        <path d="M34 28 Q50 16 66 28 V40 H34 Z"/>
        <path d="M35 40 Q35 58 50 58 Q65 58 65 40"/>
        <path d="M18 80 Q20 62 38 60 L50 72 L62 60 Q80 62 82 80 Z"/>
      </g>
      <path d="M50 24 V34 M45 29 H55" stroke="#1e44a0" stroke-width="3"/>
    </svg>
    <h3 class="service-name" style="top:834px">Registered Nurses</h3>
  </section>

  <section class="service" style="top:0">
    <svg class="service-icon" style="top:1062px" viewBox="0 0 100 100" aria-hidden="true">
      <circle cx="50" cy="50" r="50" fill="#fff"/>
      <g stroke="#1e44a0" stroke-width="5" fill="none" stroke-linejoin="round">
        <path d="M26 62 Q26 38 44 34 V24 H56 V34 Q74 38 74 62"/>
        <rect x="14" y="62" width="72" height="12"/>
      </g>
    </svg>
    <h3 class="service-name" style="top:1016px">On-site Remote and<br>Offshore Health and<br>Safety</h3>
  </section>

  <section class="service" style="top:0">
    <svg class="service-icon" style="top:1328px" viewBox="0 0 100 100" aria-hidden="true">
      <circle cx="50" cy="50" r="50" fill="#fff"/>
      <g stroke="#1e44a0" stroke-width="7" stroke-linecap="butt">
        <path d="M50 12 V88 M12 50 H88 M23 23 L77 77 M77 23 L23 77"/>
      </g>
    </svg>
    <h3 class="service-name" style="top:1358px">Emergency Medical Aid</h3>
  </section>

  <section class="service" style="top:0">
    <svg class="service-icon" style="top:1571px" viewBox="0 0 100 100" aria-hidden="true">
      <circle cx="50" cy="50" r="50" fill="#fff"/>
      <g fill="#1e44a0" stroke="#1e44a0" stroke-width="5">
        <circle cx="50" cy="50" r="18"/>
        <path d="M50 14 V86 M14 50 H86 M25 25 L75 75 M75 25 L25 75"/>
      </g>
      <g fill="#1e44a0">
        <circle cx="50" cy="13" r="7"/><circle cx="50" cy="87" r="7"/>
        <circle cx="13" cy="50" r="7"/><circle cx="87" cy="50" r="7"/>
        <circle cx="24" cy="24" r="7"/><circle cx="76" cy="76" r="7"/>
        <circle cx="76" cy="24" r="7"/><circle cx="24" cy="76" r="7"/>
      </g>
      <circle cx="50" cy="50" r="7" fill="#fff"/>
    </svg>
    <h3 class="service-name" style="top:1539px">COVID-19 Screening<br>and Monitoring</h3>
  </section>

  <div class="photo" role="img" aria-label="Photo of a white and green medical helicopter parked on a tarmac under an overcast sky"></div>

  <div class="slogan-band">
    <p class="slogan">No Place is Safer than Us</p>
  </div>

  <div class="brand">
    <div class="brand-dot" aria-hidden="true"></div>
    <h1 class="brand-name">VOREN</h1>
  </div>
</main>
</body>
</html>
```